Startup online payment business - Sporting / Golf, Swift Tee payment

Background:
Our business name is "Swift Tee" we provide online payments for golfing services via our website. We currently have a logo used on our website. No other design style has been developed. Our aim is to remove cash payments for service at golf clubs.

Our Key Values:
Quick and easy
Formal and polite
Fun with professional boundary
Mate-ship relationships
100% online digital

What we want from you:
Marketing design to be used on posters and stickers in a retail setting to direct customers to our online payment Chanel.
Design must incorporate attached logo, URL swifttee.com.au and our key values can act as a guide the type of design. We have used color Hex#007672 for logo background. We are open to use other colors.

Target Market(s)

Golf clubs and golf players

Industry/Entity Type

Golf Course

Font styles to use
Sans Serif

Requirements
Must have
• Directions to online payment via URL: swifttee.com.au
Nice to have
• We like the idea of the slogan: No Cash - No worries. Have attached home screen that will be available from URL link. Consideration if using mobile phone in image. Push the online payment and steps 1. Visit swifttee.com 2. Select club 3. Confirm payment
Should not have
• Cartoons

```html
<!DOCTYPE html>
<html lang="en">
<head>
<meta charset="UTF-8">
<title>Swift Tee – No Cash No Worries Poster</title>
<link href="https://fonts.googleapis.com/css2?family=Anton&family=Montserrat:wght@400;700&display=swap" rel="stylesheet">
<style>
  :root {
    --page-bg: #ebebeb;
    --teal-top: #1b9a92;
    --teal-bottom: #0b817b;
    --teal-band: #0aa6a0;
    --teal-dark: #06706b;
    --cyan-bright: #16e0da;
    --cyan-deep: #0aa39d;
    --white: #ffffff;
    --icon-ring: #0b9a94;
  }
  * { margin: 0; padding: 0; box-sizing: border-box; }
  html, body { width: 1200px; height: 1200px; overflow: hidden; background: var(--page-bg); }
  .poster {
    position: absolute; left: 197px; top: 30px; width: 806px; height: 1140px;
    background: linear-gradient(180deg, var(--teal-top) 0%, var(--teal-bottom) 100%);
    overflow: hidden; font-family: 'Montserrat', sans-serif; color: var(--white);
  }
  .golfer-photo {
    position: absolute; left: 470px; top: 30px; width: 290px; height: 1020px;
    background: linear-gradient(180deg, rgba(120,170,190,0.45) 0%, rgba(150,160,165,0.5) 35%, rgba(215,212,195,0.55) 70%, rgba(160,150,130,0.5) 100%);
    border-radius: 120px 120px 10px 10px;
  }
  .brand-name {
    position: absolute; left: 71px; top: 100px;
    font-family: 'Anton', sans-serif; font-size: 64px; letter-spacing: 4px; color: var(--white);
  }
  .headline { position: absolute; left: 66px; top: 255px; font-family: 'Anton', sans-serif; line-height: 1; }
  .headline-top { display: block; font-size: 126px; color: var(--white); }
  .headline-bottom {
    display: block; font-size: 126px; margin-top: -14px;
    background: linear-gradient(180deg, var(--cyan-bright) 0%, var(--cyan-deep) 100%);
    -webkit-background-clip: text; background-clip: text; color: transparent;
  }
  .intro { position: absolute; left: 67px; top: 500px; font-size: 24px; line-height: 1.35; font-weight: 400; }
  .values-band {
    position: absolute; left: 0; top: 581px; width: 353px; height: 64px;
    background: var(--teal-band); border-radius: 0 32px 32px 0;
    display: flex; align-items: center; padding-left: 67px;
    font-size: 24px; font-weight: 700; letter-spacing: 0.5px;
  }
  .value-list { position: absolute; left: 67px; top: 665px; list-style: none; }
  .value-item { display: flex; align-items: center; height: 78px; }
  .value-icon {
    width: 64px; height: 64px; border-radius: 50%;
    border: 2px solid var(--icon-ring); background: var(--teal-dark);
    display: flex; align-items: center; justify-content: center; margin-right: 12px; flex-shrink: 0;
  }
  .value-icon svg { width: 38px; height: 38px; fill: none; stroke: var(--white); stroke-width: 1.6; stroke-linecap: round; stroke-linejoin: round; }
  .value-text { font-size: 20px; font-weight: 700; line-height: 1.2; }
  .cta {
    position: absolute; left: 51px; top: 1070px; width: 702px; height: 46px;
    background: var(--teal-band); border-radius: 23px; display: flex; align-items: center;
  }
  .cta-label { font-size: 20px; font-weight: 700; margin-left: 26px; width: 291px; letter-spacing: 0.3px; }
  .cta-url {
    background: var(--teal-dark); border-radius: 13px; height: 26px; width: 367px;
    display: flex; align-items: center; justify-content: center;
    font-size: 19px; font-weight: 700; letter-spacing: 4px;
  }
</style>
</head>
<body>
  <main class="poster">
    <div class="golfer-photo" role="img" aria-label="Photo of a golfer in a blue cap holding a putter and checking his mobile phone"></div>

    <div class="brand-name">SWIFT TEE</div>

    <h1 class="headline">
      <span class="headline-top">NO CASH</span>
      <span class="headline-bottom">NO WORRIES</span>
    </h1>

    <p class="intro">We provide online payments for<br>golfing services via our website</p>

    <div class="values-band">OUR KEY VALUES:</div>

    <ul class="value-list">
      <li class="value-item">
        <span class="value-icon"><svg viewBox="0 0 40 40"><circle cx="22" cy="22" r="12"/><path d="M22 15v7l4 3M19 6h6M22 6v4M4 18h6M2 23h7M5 28h6"/></svg></span>
        <span class="value-text">Quick<br>and easy</span>
      </li>
      <li class="value-item">
        <span class="value-icon"><svg viewBox="0 0 40 40"><path d="M12 6l8 6 8-6 6 6-3 18-11 6-11-6-3-18z"/><path d="M20 12v22M16 10l4 6 4-6"/></svg></span>
        <span class="value-text">Formal<br>and polite</span>
      </li>
      <li class="value-item">
        <span class="value-icon"><svg viewBox="0 0 40 40"><rect x="16" y="5" width="18" height="30" rx="1"/><path d="M19 11l2 2 3-3M26 12h5M19 19l2 2 3-3M26 20h5M19 27l2 2 3-3M26 28h5"/><circle cx="9" cy="14" r="3"/><path d="M4 34V22a5 5 0 0 1 10 0v12"/></svg></span>
        <span class="value-text">Fun with<br>professional boundary</span>
      </li>
      <li class="value-item">
        <span class="value-icon"><svg viewBox="0 0 40 40"><path d="M20 14s-6-4-6-8a3 3 0 0 1 6-1 3 3 0 0 1 6 1c0 4-6 8-6 8z"/><path d="M20 16v5M8 21h24M8 21v4M20 21v4M32 21v4"/><circle cx="8" cy="28" r="2.5"/><circle cx="20" cy="28" r="2.5"/><circle cx="32" cy="28" r="2.5"/><path d="M4 36a4 4 0 0 1 8 0M16 36a4 4 0 0 1 8 0M28 36a4 4 0 0 1 8 0"/></svg></span>
        <span class="value-text">Mate-ship<br>relationships</span>
      </li>
      <li class="value-item">
        <span class="value-icon"><svg viewBox="0 0 40 40"><rect x="4" y="4" width="16" height="32" rx="2"/><path d="M10 32h4"/><rect x="14" y="12" width="22" height="14" rx="2"/><path d="M14 17h22"/><circle cx="28" cy="30" r="6"/><path d="M28 26v8M30 28h-3a1 1 0 0 0 0 2h2a1 1 0 0 1 0 2h-3"/></svg></span>
        <span class="value-text">100%<br>online digital</span>
      </li>
    </ul>

    <div class="cta">
      <span class="cta-label">VISIT OUR WEBSITE NOW</span>
      <span class="cta-url">www.swifttee.com.au</span>
    </div>
  </main>
</body>
</html>
```